Southern Trade Depot needs a label designed for a new product

we need a label designed for a new product (Trowel Mate) but since its new to the market we want the label to be based on the design of the top 2 existing brands so it is instantly familiar with the customer, attached a photo of the 2 different brands that it needs to look like

Target Market(s)

BRICKLAYERS/ BUILDERS

Industry/Entity Type

Building Product

Requirements
Must have
• MUST HAVE SIMULAR FEELS AS THE UPLOADED IMAGE AND FEEL FAMILIAR WITH THOSE BRANDS

```html
<!DOCTYPE html>
<html lang="en">
<head>
<meta charset="utf-8">
<title>Trowel Mate – 20 kg Bag Label</title>
<link rel="stylesheet" href="https://fonts.googleapis.com/css2?family=Arimo:wght@700&display=swap">
<style>
  :root {
    --paper: #ffffff;
    --bag-grey: #e0dfdd;
    --band-orange: #e87305;
    --band-black: #000000;
    --brand-blue: #0b4f82;
    --product-navy: #10446c;
    --ink-black: #000000;
    --ink-white: #fbf9fa;
    --tool-grey: #d9d9d9;
  }
  html, body {
    margin: 0;
    padding: 0;
    overflow: hidden;
    background: var(--paper);
  }
  .label {
    position: relative;
    width: 859px;
    height: 1200px;
    overflow: hidden;
    background: var(--paper);
    font-family: "Arimo", Arial, sans-serif;
    font-weight: 700;
  }
  .label__face {
    position: absolute;
    left: 7px;
    top: 10px;
    width: 844px;
    height: 1180px;
    background: var(--bag-grey);
  }
  .text {
    position: absolute;
    left: 0;
    width: 859px;
    margin: 0;
    text-align: center;
    line-height: 1;
    white-space: nowrap;
  }
  .brand__name {
    top: 168px;
    font-size: 50px;
    color: var(--ink-black);
  }
  .band--orange {
    position: absolute;
    left: 7px;
    width: 844px;
    top: 448px;
    height: 314px;
    background: var(--band-orange);
  }
  .band--black {
    position: absolute;
    left: 7px;
    width: 844px;
    top: 485px;
    height: 114px;
    background: var(--band-black);
  }
  .product__line1 {
    top: 481px;
    font-size: 125px;
    color: var(--ink-white);
  }
  .product__line2 {
    top: 606px;
    font-size: 147px;
    color: var(--product-navy);
  }
  .product__tool {
    position: absolute;
    left: 304px;
    top: 799px;
    width: 253px;
    height: 146px;
    background: linear-gradient(160deg, var(--bag-grey), var(--tool-grey));
    border-radius: 6px;
  }
  .benefit {
    font-size: 23.5px;
    color: var(--brand-blue);
  }
  .benefit--one { top: 995px; }
  .benefit--two { top: 1023px; }
  .net-weight {
    position: absolute;
    left: 570px;
    top: 1108px;
    margin: 0;
    font-size: 35px;
    line-height: 1;
    color: var(--brand-blue);
  }
</style>
</head>
<body>
  <main class="label">
    <div class="label__face"></div>

    <p class="text brand__name">SOUTHERN TRADE DEPOT</p>

    <div class="band--orange"></div>
    <div class="band--black"></div>
    <h1 class="text product__line1">TROWEL</h1>
    <p class="text product__line2">MATE</p>

    <div class="product__tool" role="img" aria-label="Line drawing of a bricklayer's trowel"></div>

    <p class="text benefit benefit--one">BLENDS WITH SAND AND CEMENT FOR MPRTAR</p>
    <p class="text benefit benefit--two">ENHANCES MORTAR BOND STRENGTH AND WORKABILITY</p>

    <p class="net-weight">20 KGS.</p>
  </main>
</body>
</html>
```